Harbor Wonder Hour - A magic website for a monthly modern magic show

Looking to build a website to promote my new monthly magic show

Sites like this. https://velvetloftshow.example/ https://brasslanterntricks.example/

Target Market(s)

18-65 year old men and women who enjoy live entertainment especially magic

Industry/Entity Type

Entertainment

Coding

Coded - Design and coding required

Number of Pages Required

3 page

Colors

Designer to choose colors to be used in the design.

Requirements
Must have
• Wanting a wordpress site.
• Contact form, media section for photos and videos to be posted.
• A “reviews/testimonials” section.

```html
<!DOCTYPE html>
<html lang="en">
<head>
<meta charset="utf-8">
<title>Harbor Wonder Hour</title>
<link rel="stylesheet" href="https://fonts.googleapis.com/css2?family=Poppins:wght@300;400;500;600;700&display=swap">
<style>
:root{
  --bg:#1a1919;
  --bg-deep:#121111;
  --ink:#ffffff;
  --muted:#a9a6a3;
  --faint:#6f6b68;
  --line:#3a3837;
  --photo-dark:#232120;
  --photo-mid:#3a3532;
  --smoke:#5a4b42;
  --ember:#8a2a22;
}
*{box-sizing:border-box;margin:0;padding:0}
html,body{width:1200px;height:4184px;overflow:hidden;background:var(--bg);}
body{position:relative;font-family:"Poppins",sans-serif;color:var(--ink);}
.abs{position:absolute}
.photo{position:absolute}
.logo{left:110px;top:22px;font-weight:700;font-size:22px;line-height:24px;}
.nav{left:505px;top:44px;display:flex;gap:44px;font-size:11px;color:#ddd}
.social{display:flex;gap:8px}
.social span{display:block;width:16px;height:16px;border-radius:50%;background:#cfcfcf}
.head-social{left:1036px;top:40px}
.hero-title{left:0;width:1200px;top:290px;text-align:center;font-size:64px;font-weight:300;letter-spacing:12px}
.hero-title b{font-weight:700}
.hero-copy{left:330px;width:540px;top:380px;text-align:center;font-size:10px;line-height:16px;color:#cfcbc8}
.btn{display:inline-block;background:#fff;color:#111;font-size:9px;font-weight:500;letter-spacing:1px;text-transform:uppercase;padding:0;width:96px;height:28px;line-height:28px;text-align:center}
.scroll{left:0;width:1200px;top:640px;text-align:center;font-size:9px;color:#ccc}
h2{font-weight:300;letter-spacing:4px;font-size:36px}
h2 b{font-weight:700}
.sub{font-weight:600;font-size:15px;letter-spacing:1px}
.copy{font-size:10px;line-height:17px;color:var(--muted)}
.gal-cap{font-size:10px;line-height:16px;color:#cfcbc8}
.field{position:absolute;border:1px solid #5a5756;font-size:9px;color:#8c8886;padding:5px 7px}
.foot-h{font-size:12px;font-weight:500;letter-spacing:2px}
.links{font-size:10px;line-height:18px;color:var(--muted)}
</style>
</head>
<body>

<!-- Hero backdrop -->
<div class="photo" role="img" aria-label="Magician in a dark room fanning playing cards" style="left:0;top:0;width:1200px;height:820px;background:radial-gradient(ellipse at 55% 35%,#3a3431 0%,#211f1e 45%,var(--bg) 80%)"></div>
<div class="photo" role="img" aria-label="Playing card flying through the air" style="left:1005px;top:230px;width:80px;height:105px;transform:rotate(18deg);background:linear-gradient(135deg,#e9e4e0,#b9b2ad);border-radius:5px"></div>
<div class="photo" role="img" aria-label="Blurred playing card in motion" style="left:20px;top:600px;width:130px;height:155px;transform:rotate(-28deg);background:linear-gradient(135deg,#ddd8d4,#8f8985);border-radius:6px;opacity:.8"></div>

<header>
  <div class="abs logo">Harbor<br><span style="font-size:11px;font-weight:400">Wonder Hour</span></div>
  <nav class="abs nav"><span>Home</span><span>Reviews</span><span>Film</span><span>Private Events</span></nav>
  <div class="abs social head-social"><span></span><span></span></div>
</header>

<section class="hero">
  <h1 class="abs hero-title">UNFOR<b>GETTABLE</b></h1>
  <p class="abs hero-copy">An evening of sleight of hand, mind reading and impossible moments,<br>staged live every month in an intimate harbor side room with guests.</p>
  <div class="abs" style="left:552px;top:452px"><span class="btn">Watch Video</span></div>
  <div class="abs scroll">
    <svg width="12" height="40" viewBox="0 0 12 40" style="display:block;margin:0 auto 6px"><line x1="6" y1="0" x2="6" y2="36" stroke="#ccc"/><path d="M2 32l4 6 4-6" fill="none" stroke="#ccc"/></svg>
    Scroll Down
  </div>
</section>

<section class="about">
  <div class="photo" role="img" aria-label="Open hand tossing dice in the dark" style="left:80px;top:860px;width:440px;height:320px;background:radial-gradient(ellipse at 60% 50%,#3b3431 0%,#1f1d1c 55%,var(--bg) 85%)"></div>
  <h2 class="abs" style="left:580px;top:940px;font-size:30px"><b>ABOUT</b> US</h2>
  <p class="abs sub" style="left:580px;top:1000px;font-size:13px">Lorem Ipsum Is Simply Dummy Text</p>
  <p class="abs copy" style="left:580px;top:1060px;width:520px">Every month we open the doors to a small audience for a close up show built around cards, coins and borrowed objects. Our performers mix classic technique with modern storytelling so every trick feels personal. Guests sit just a few feet away, close enough to check every move and still wonder how it happened. Come early, grab a drink and settle in for ninety minutes of laughter, suspense and genuine astonishment that will stay with you long after the final bow.</p>
</section>

<section class="experience">
  <div class="photo" role="img" aria-label="Curling smoke against a black background" style="left:620px;top:1420px;width:420px;height:700px;background:radial-gradient(ellipse at 50% 45%,var(--smoke) 0%,#2d2624 35%,var(--bg) 70%);opacity:.85"></div>
  <h2 class="abs" style="left:185px;top:1580px;font-size:30px"><b>HARBOR</b> WONDER</h2>
  <p class="abs sub" style="left:185px;top:1670px;font-size:13px">IS AN INTERACTIVE MAGIC EXPERIENCE</p>
  <p class="abs copy" style="left:185px;top:1705px;width:420px">You are not just watching, you are part of the act. Volunteers shuffle, choose and sign, while the whole room helps build each impossible finale. Every show is different, shaped by the people in the seats and the stories they bring along.</p>
  <div class="abs" style="left:185px;top:1846px"><span class="btn">Book Tickets</span></div>
</section>

<section class="gallery">
  <h2 class="abs" style="left:0;width:1200px;text-align:center;top:2205px;font-size:30px"><b>PHOTOS</b> &amp; <b>VIDEOS</b></h2>
  <div class="photo" role="img" aria-label="Performer breathing red smoke" style="left:120px;top:2340px;width:265px;height:280px;background:radial-gradient(ellipse at 55% 30%,var(--ember) 0%,#3a1d1a 40%,#161414 85%)"></div>
  <p class="abs gal-cap" style="left:145px;top:2510px;width:230px">Lorem ipsum stage moments captured from the front row.</p>
  <div class="photo" role="img" aria-label="Magician framed by hands in a video still" style="left:395px;top:2345px;width:260px;height:230px;background:radial-gradient(ellipse at 50% 50%,#4a4542 0%,#2a2726 60%,#1c1b1a 100%)"></div>
  <svg class="abs" style="left:505px;top:2440px" width="40" height="40" viewBox="0 0 40 40"><circle cx="20" cy="20" r="20" fill="#fff"/><path d="M16 12l12 8-12 8z" fill="#111"/></svg>
  <div class="photo" role="img" aria-label="Magician in a denim jacket performing a card trick" style="left:120px;top:2600px;width:535px;height:300px;background:linear-gradient(120deg,#2a2726 0%,#4b4440 45%,#2b2827 100%)"></div>
  <svg class="abs" style="left:340px;top:2732px" width="40" height="40" viewBox="0 0 40 40"><circle cx="20" cy="20" r="20" fill="#fff"/><path d="M16 12l12 8-12 8z" fill="#111"/></svg>
  <div class="photo" role="img" aria-label="Portrait of the magician smoking in low light" style="left:690px;top:2370px;width:430px;height:530px;background:radial-gradient(ellipse at 55% 35%,#3c3735 0%,#242221 55%,#1b1a19 100%)"></div>
  <p class="abs" style="left:745px;top:2680px;font-size:11px;font-weight:600;letter-spacing:2px">MEET THE MAGICIAN</p>
  <p class="abs copy" style="left:745px;top:2715px;width:260px;color:#c8c4c1">Raised on old card books and street shows, our host has spent years refining a quiet, clever style that turns a simple deck into pure drama for every single guest.</p>
  <div class="abs" style="left:552px;top:2986px"><span class="btn">View More</span></div>
</section>

<section class="testimonials">
  <h2 class="abs" style="left:0;width:1200px;text-align:center;top:3220px;font-size:30px"><b>CLIENTS</b> TESTIMONIALS</h2>
  <div class="photo" role="img" aria-label="Guest portrait, faded" style="left:500px;top:3350px;width:60px;height:60px;border-radius:50%;background:#4a4644;opacity:.5"></div>
  <div class="photo" role="img" aria-label="Guest portrait, faded" style="left:640px;top:3350px;width:60px;height:60px;border-radius:50%;background:#4a4644;opacity:.5"></div>
  <div class="photo" role="img" aria-label="Portrait of reviewer Marcus Delane" style="left:558px;top:3338px;width:84px;height:84px;border-radius:50%;border:3px solid #fff;background:linear-gradient(160deg,#cfd6dd,#6f7a86)"></div>
  <svg class="abs" style="left:222px;top:3432px" width="12" height="18" viewBox="0 0 12 18"><path d="M10 1L2 9l8 8" fill="none" stroke="#ccc" stroke-width="2"/></svg>
  <svg class="abs" style="left:966px;top:3432px" width="12" height="18" viewBox="0 0 12 18"><path d="M2 1l8 8-8 8" fill="none" stroke="#ccc" stroke-width="2"/></svg>
  <p class="abs copy" style="left:350px;width:500px;top:3475px;text-align:center;color:#c8c4c1">We came for a birthday and left completely stunned. The tricks happened inches from our faces and we still cannot explain a single one. Warm host, great room, and the best night out we have had in years.</p>
  <p class="abs" style="left:0;width:1200px;text-align:center;top:3612px;font-size:11px;letter-spacing:2px"><b>MARCUS DELANE</b> <span style="color:var(--faint)">| Guest</span></p>
</section>

<footer>
  <div class="abs" style="left:120px;top:3770px;width:960px;height:1px;background:var(--line)"></div>
  <div class="abs logo" style="left:190px;top:3830px">Harbor<br><span style="font-size:11px;font-weight:400">Wonder Hour</span></div>
  <p class="abs links" style="left:190px;top:3885px;width:200px">Address<br>14 Lantern Quay, Suite 3<br>Harbor City, Old Town<br>Tel: 555 014 2290</p>
  <div class="abs social" style="left:190px;top:4002px"><span></span><span></span></div>
  <p class="abs" style="left:190px;top:4140px;font-size:8px;color:var(--faint)">Harbor Wonder Hour Copyright 2019</p>

  <p class="abs foot-h" style="left:430px;top:3848px">USEFUL LINKS</p>
  <p class="abs links" style="left:430px;top:3895px">Home<br>About<br>Reviews<br>Film<br>Private Events</p>

  <p class="abs foot-h" style="left:745px;top:3848px">GET IN TOUCH</p>
  <div class="field" style="left:745px;top:3893px;width:118px;height:26px">Name*</div>
  <div class="field" style="left:875px;top:3893px;width:118px;height:26px">Email*</div>
  <div class="field" style="left:745px;top:3931px;width:118px;height:26px">Phone No.</div>
  <div class="field" style="left:745px;top:3969px;width:248px;height:90px">Message</div>
  <div class="abs" style="left:745px;top:4088px"><span class="btn" style="width:86px;height:26px;line-height:26px">Send</span></div>
</footer>

</body>
</html>
```